Drywall plastering business card design

Attached is my new logo and a picture of my current business card. I would like my new logo incorporated in to the business card and also my website which is:
www.kowhaibaywallcraftsolutions.co.nz
Industry/Entity Type
Business
Contact Information for Business Card
I would like a picture of my van and my new logo on my new business card. See attached files for pictures of my old business card, van picture and logo.
Colors
0555a3
ffffff
Requirements
Must have
- New logo, Van, contact info

```html
<!DOCTYPE html>
<html lang="en">
<head>
<meta charset="utf-8">
<title>Kowhai Bay Wallcraft Solutions – Business Card</title>
<link rel="stylesheet" href="https://fonts.googleapis.com/css2?family=Open+Sans:wght@400;600;700;800&family=Roboto+Condensed:wght@400&display=swap">
<style>
  :root {
    --brand-blue: #0a7fd0;
    --brand-blue-deep: #0555a3;
    --card-white: #ffffff;
    --ink: #222222;
    --ink-soft: #444444;
    --backdrop: #3b3b3d;
    --divider: #e6e6e6;
  }
  * { box-sizing: border-box; margin: 0; padding: 0; }
  html, body {
    width: 1200px; height: 852px; overflow: hidden;
    background: var(--backdrop);
    font-family: "Open Sans", Arial, sans-serif;
  }
  .stage { position: relative; width: 1200px; height: 852px; }

  .card {
    position: absolute;
    width: 560px; height: 320px;
    border-radius: 14px;
    overflow: hidden;
    box-shadow: 0 12px 30px rgba(0,0,0,0.45);
  }

  /* Front */
  .card-front {
    left: 150px; top: 100px;
    background: var(--brand-blue);
    display: flex; align-items: center; justify-content: center;
  }
  .brand-mark {
    display: flex; align-items: center; gap: 14px;
  }
  .brand-mark .mark-square {
    width: 22px; height: 22px; flex: none;
  }
  .brand-name {
    font-weight: 800; text-transform: uppercase;
    line-height: 1.05; letter-spacing: 0.5px;
  }
  .card-front .brand-name { color: var(--card-white); font-size: 34px; }
  .card-front .mark-square { background: var(--card-white); }

  /* Back */
  .card-back {
    left: 490px; top: 440px;
    background: var(--card-white);
  }
  .card-back .bottom-band {
    position: absolute; left: 0; right: 0; bottom: 0; height: 10px;
    background: var(--brand-blue);
  }
  .card-back .divider {
    position: absolute; left: 0; top: 0; width: 100%; height: 100%;
  }
  .card-back .logo-area {
    position: absolute; left: 28px; top: 0; bottom: 10px; width: 250px;
    display: flex; align-items: center;
  }
  .card-back .brand-name { color: var(--brand-blue); font-size: 24px; }
  .card-back .mark-square { background: var(--brand-blue); }

  .details {
    position: absolute; left: 300px; top: 34px; right: 24px;
  }
  .person-name {
    color: var(--brand-blue); font-weight: 700; font-size: 17px;
    letter-spacing: 0.3px;
  }
  .person-title {
    color: var(--ink-soft); font-size: 12px; margin-top: 2px; margin-left: 14px;
  }
  .contact-list {
    list-style: none; margin-top: 36px;
    font-family: "Roboto Condensed", Arial, sans-serif;
    font-size: 12px; color: var(--ink);
  }
  .contact-list li {
    display: flex; align-items: center; gap: 8px; margin-bottom: 7px;
    white-space: nowrap;
  }
  .contact-list svg { width: 12px; height: 12px; flex: none; fill: var(--brand-blue); }
  .tagline {
    margin-top: 8px; margin-left: 20px;
    color: var(--brand-blue); font-size: 14px; line-height: 1.35;
    text-transform: uppercase;
  }
</style>
</head>
<body>
<main class="stage">

  <section class="card card-front" aria-label="Business card front">
    <div class="brand-mark">
      <span class="mark-square"></span>
      <span class="brand-name">Kowhai Bay<br>Wallcraft<br>Solutions</span>
    </div>
  </section>

  <section class="card card-back" aria-label="Business card back">
    <svg class="divider" viewBox="0 0 560 320" preserveAspectRatio="none" aria-hidden="true">
      <path d="M285 0 L260 160 L285 310" stroke="var(--divider)" stroke-width="1.5" fill="none"/>
    </svg>

    <div class="logo-area">
      <div class="brand-mark">
        <span class="mark-square"></span>
        <span class="brand-name">Kowhai Bay<br>Wallcraft<br>Solutions</span>
      </div>
    </div>

    <div class="details">
      <p class="person-name">MARK TANE</p>
      <p class="person-title">Proprietor</p>

      <ul class="contact-list">
        <li>
          <svg viewBox="0 0 24 24" aria-hidden="true"><path d="M6.6 10.8a15.1 15.1 0 0 0 6.6 6.6l2.2-2.2c.3-.3.7-.4 1-.2 1.1.4 2.3.6 3.6.6.6 0 1 .4 1 1V20c0 .6-.4 1-1 1C10.6 21 3 13.4 3 4c0-.6.4-1 1-1h3.5c.6 0 1 .4 1 1 0 1.3.2 2.5.6 3.6.1.3 0 .7-.2 1z"/></svg>
          <span>027 555 01 42</span>
        </li>
        <li>
          <svg viewBox="0 0 24 24" aria-hidden="true"><path d="M2 5h20v14H2z M4 7v.5l8 5 8-5V7l-8 5z" fill-rule="evenodd"/></svg>
          <span>kowhaibaywallcraft@gmail.com</span>
        </li>
        <li>
          <svg viewBox="0 0 24 24" aria-hidden="true"><path d="M12 2a10 10 0 1 0 0 20 10 10 0 0 0 0-20zm6.9 6h-3a15.7 15.7 0 0 0-1.3-3.6A8 8 0 0 1 18.9 8zM12 4c.8 1.2 1.5 2.5 1.9 4h-3.8c.4-1.5 1.1-2.8 1.9-4zM4.3 14a8 8 0 0 1 0-4h3.4a16 16 0 0 0 0 4zm.8 2h3a15.7 15.7 0 0 0 1.3 3.6A8 8 0 0 1 5.1 16zm3-8h-3a8 8 0 0 1 4.3-3.6A15.7 15.7 0 0 0 8.1 8zM12 20c-.8-1.2-1.5-2.5-1.9-4h3.8c-.4 1.5-1.1 2.8-1.9 4zm2.3-6H9.7a14.7 14.7 0 0 1 0-4h4.6a14.7 14.7 0 0 1 0 4zm.3 5.6c.6-1.1 1-2.3 1.3-3.6h3a8 8 0 0 1-4.3 3.6zm1.7-5.6a16 16 0 0 0 0-4h3.4a8 8 0 0 1 0 4z"/></svg>
          <span>www.kowhaibaywallcraftsolutions.co.nz</span>
        </li>
      </ul>

      <p class="tagline">Large jobs or small -<br>always quality assured</p>
    </div>

    <div class="bottom-band"></div>
  </section>

</main>
</body>
</html>
```